business card and stationary for a auto race team
Tolland Racing
Cutting-Edge
Ross Tolland
5678 Elm Lane Fairbrook, NY, 22222
postbox@velmarsh.net
I must be able to add all information, name, address, city, state, zip code, phone number and email address.
logo can be found as winner of Tolland Racing logo design

```html
<!DOCTYPE html>
<html lang="en">
<head>
<meta charset="utf-8">
<title>Tolland Racing Stationery</title>
<link href="https://fonts.googleapis.com/css2?family=Rajdhani:wght@500;700&display=swap" rel="stylesheet">
<style>
:root{
  --bg:#e9e6e1;
  --red:#d71920;
  --red-dark:#a80f14;
  --black:#1b1b1d;
  --paper:#ffffff;
  --ink:#2a2a2a;
  --grey:#9a9a9a;
  --faint:#f1e4e4;
}
*{margin:0;padding:0;box-sizing:border-box}
html,body{width:1200px;height:206px;overflow:hidden;background:var(--bg);font-family:'Rajdhani',sans-serif;color:var(--ink)}
.canvas{position:relative;width:1200px;height:206px}
.piece{position:absolute;background:var(--paper);box-shadow:0 1px 3px rgba(0,0,0,.25)}
.dark{background:var(--black);color:#fff}
.red{background:var(--red);color:#fff}
.brand{font-weight:700;color:var(--red);line-height:1;white-space:nowrap;display:flex;align-items:center;gap:3px}
.brand::before{content:"";width:.7em;height:.7em;background:currentColor;display:inline-block}
.dark .brand,.red .brand{color:#fff}
.dark .brand.on-red{color:var(--red)}
.small{font-size:5px;line-height:1.35;font-weight:500}
.center{display:flex;flex-direction:column;align-items:center;justify-content:center}
.band{position:absolute;left:0;right:0;height:5px;background:var(--red)}
.body-lines{margin-top:10px}
.body-lines p{font-size:4px;color:var(--grey);margin-bottom:2px}
.ghost{position:absolute;font-weight:700;color:var(--faint);font-size:26px;white-space:nowrap}
</style>
</head>
<body>
<div class="canvas">

  <!-- business cards, front and back -->
  <div class="piece dark center" style="left:12px;top:22px;width:96px;height:56px">
    <div class="brand on-red" style="font-size:11px">Tolland Racing</div>
    <div class="small" style="color:#bbb;margin-top:3px">Cutting-Edge</div>
  </div>
  <div class="piece dark" style="left:12px;top:108px;width:96px;height:56px;padding:8px">
    <div class="brand on-red" style="font-size:7px">Tolland Racing</div>
    <div class="small" style="margin-top:8px;color:#fff">Ross Tolland</div>
    <div class="small" style="color:#bbb">Team Manager</div>
    <div class="small" style="color:#bbb">5678 Elm Lane Fairbrook, NY, 22222</div>
    <div class="small" style="color:#bbb">postbox@velmarsh.net</div>
  </div>

  <!-- letterhead -->
  <div class="piece" style="left:116px;top:18px;width:124px;height:170px;padding:10px">
    <div class="brand" style="font-size:9px">Tolland Racing</div>
    <div class="body-lines">
      <p>Dear Partner,</p>
      <p>Thank you for your support this season.</p>
    </div>
    <div class="small" style="position:absolute;bottom:8px;left:10px;color:var(--grey)">5678 Elm Lane Fairbrook, NY, 22222 · postbox@velmarsh.net</div>
    <div class="band" style="bottom:0;height:3px"></div>
  </div>

  <!-- card set -->
  <div class="piece dark center" style="left:250px;top:40px;width:70px;height:40px">
    <div class="brand on-red" style="font-size:8px">Tolland Racing</div>
  </div>
  <div class="piece" style="left:250px;top:90px;width:70px;height:40px;padding:5px">
    <div class="brand" style="font-size:6px">Tolland Racing</div>
    <div class="small" style="margin-top:5px;font-size:4px">Ross Tolland</div>
    <div class="small" style="font-size:4px;color:var(--grey)">postbox@velmarsh.net</div>
  </div>
  <div class="piece" style="left:330px;top:30px;width:62px;height:36px;padding:5px">
    <div class="brand" style="font-size:6px">Tolland Racing</div>
    <div class="band" style="bottom:0;height:3px"></div>
  </div>

  <!-- envelopes -->
  <div class="piece" style="left:330px;top:110px;width:140px;height:70px;padding:8px">
    <div class="brand" style="font-size:7px">Tolland Racing</div>
    <div class="small" style="color:var(--grey)">5678 Elm Lane Fairbrook, NY, 22222</div>
  </div>
  <div class="piece" style="left:400px;top:20px;width:118px;height:60px;overflow:hidden">
    <div class="dark center" style="position:absolute;left:0;right:0;top:0;height:20px">
      <div class="brand on-red" style="font-size:7px">Tolland Racing</div>
    </div>
    <div class="band" style="top:20px;height:3px"></div>
  </div>
  <div class="piece" style="left:525px;top:20px;width:118px;height:60px;padding:8px">
    <div class="brand" style="font-size:7px">Tolland Racing</div>
    <div class="band" style="bottom:0;height:3px"></div>
  </div>
  <div class="piece" style="left:525px;top:110px;width:118px;height:70px;padding:8px">
    <div class="brand" style="font-size:7px">Tolland Racing</div>
    <div class="small" style="color:var(--grey)">postbox@velmarsh.net</div>
  </div>

  <!-- folder -->
  <div class="piece red" style="left:760px;top:14px;width:110px;height:178px">
    <div class="dark" style="position:absolute;left:0;right:0;bottom:0;height:40px;background:var(--red-dark)"></div>
  </div>
  <div class="piece center" style="left:870px;top:14px;width:110px;height:178px">
    <div class="brand" style="font-size:11px">Tolland Racing</div>
    <div class="small" style="color:var(--grey);margin-top:3px">Cutting-Edge</div>
    <div class="band" style="bottom:0;height:6px"></div>
  </div>
  <div class="piece" style="left:900px;top:150px;width:40px;height:24px;padding:4px">
    <div class="brand" style="font-size:4px">Tolland Racing</div>
  </div>

  <!-- letterheads right -->
  <div class="piece" style="left:990px;top:18px;width:100px;height:170px;padding:9px">
    <div class="brand" style="font-size:8px">Tolland Racing</div>
    <div class="band" style="bottom:0;height:3px"></div>
  </div>
  <div class="piece" style="left:1096px;top:18px;width:100px;height:170px;padding:9px;overflow:hidden">
    <div class="ghost" style="left:8px;top:60px;font-size:14px">Tolland Racing</div>
    <div class="brand" style="font-size:8px;position:relative">Tolland Racing</div>
    <div class="band" style="bottom:0;height:3px"></div>
  </div>

</div>
</body>
</html>
```